Business card design for web travel company

Hi
we'd like to receive some proposal for a business card design.
Stayvano is a private travel club, dedicated to all travel lovers, with unique offers for exclusive destinations all around the world. At Stayvano you can find a wide range of offers for resorts, boutique hotels and travel packages at the best guaranteed price available on the market. The convenience of the offer is guaranteed by a private sales model: offers are available for a limited time only and they are personally chosen by Stayvano's qualified team of travel experts.
We offer only exclusive hotels with discounted prices but we are not an outlet or a discount supermarket: the design should reflect our connection with luxury, exclusivity using the same style of our website www.stayvano-example.com.
We want to make sure that when we'll present ourself to our business partner they will feel immediately which is our brand positioning giving them also a sense of an affordable and reliable partner.
In attachment you can also find our brand guidelines (please note that we are NOT USING ANY MORE THE TAG LINE "Five star outlet" mentioned in it).
The info to be inserted are:
Name Surname
Job Title
Tel
Mobile (when needed)
Email
Stayvano S.r.l.
Via Bruno Lesta 27
20131 Milano

```html
<!DOCTYPE html>
<html lang="en">
<head>
<meta charset="utf-8">
<title>Stayvano business card – front and back</title>
<link rel="stylesheet" href="https://fonts.googleapis.com/css2?family=Exo+2:wght@300&family=Arimo:wght@400&display=swap">
<style>
  :root {
    --stage-light: #d9c89d;
    --stage-mid: #a38a5e;
    --stage-dark: #5f4523;
    --card-white: #ffffff;
    --card-charcoal: #3b3b39;
    --ink: #1d1d1b;
    --ink-soft: #3a3a3a;
    --gold: #d2c299;
    --label: #ffffff;
  }
  * { margin: 0; padding: 0; box-sizing: border-box; }
  html, body { width: 1200px; height: 1200px; overflow: hidden; }
  body {
    position: relative;
    background: radial-gradient(circle at 8% 6%, var(--stage-light) 0%, var(--stage-mid) 45%, var(--stage-dark) 100%);
    font-family: "Arimo", Arial, sans-serif;
  }
  .card {
    position: absolute;
    border-radius: 32px;
    box-shadow: 6px 8px 18px rgba(40, 25, 5, 0.35);
    overflow: hidden;
  }
  .card-front {
    left: 90px; top: 90px; width: 795px; height: 485px;
    background: var(--card-white);
  }
  .card-back {
    left: 312px; top: 622px; width: 798px; height: 488px;
    background: var(--card-charcoal);
  }
  .wordmark {
    position: absolute;
    display: flex;
    align-items: center;
    font-family: "Exo 2", "Helvetica Neue", sans-serif;
    font-weight: 300;
    letter-spacing: 0.5px;
    line-height: 1;
    white-space: nowrap;
  }
  .wordmark-mark {
    display: inline-block;
    background: var(--gold);
  }
  .card-front .wordmark {
    left: 54px; top: 62px;
    font-size: 64px;
    color: var(--ink);
  }
  .card-front .wordmark-mark { width: 16px; height: 16px; margin-left: 14px; }
  .card-back .wordmark {
    left: 0; right: 0; top: 178px;
    justify-content: center;
    font-size: 128px;
    color: var(--card-white);
  }
  .card-back .wordmark-mark { width: 30px; height: 30px; margin-left: 24px; }
  .contact {
    position: absolute;
    left: 372px; top: 192px;
    color: var(--ink-soft);
    white-space: nowrap;
  }
  .contact-name { font-size: 25px; color: var(--ink); line-height: 30px; }
  .contact-role { font-size: 18px; line-height: 26px; margin-top: 4px; }
  .contact-mobile { font-size: 22px; line-height: 28px; }
  .contact-address { font-size: 21px; line-height: 28px; margin-top: 54px; }
  .contact-line { font-size: 20px; line-height: 30px; display: flex; }
  .contact-tel { margin-top: 10px; }
  .contact-key { width: 62px; }
  .stage-label {
    position: absolute;
    color: var(--label);
    font-size: 33px;
    line-height: 1;
  }
  .stage-label-front { left: 908px; top: 548px; }
  .stage-label-back { left: 205px; top: 1080px; }
</style>
</head>
<body>
  <section class="card card-front" aria-label="Card front">
    <div class="wordmark">Stayvano<span class="wordmark-mark"></span></div>
    <div class="contact">
      <p class="contact-name">Name Surname</p>
      <p class="contact-role">Managing Director</p>
      <p class="contact-mobile">Mobile 123 456 7890</p>
      <p class="contact-address">Via Bruno Lesta 27 20131 Milano</p>
      <p class="contact-line contact-tel"><span class="contact-key">Tel</span><span>123 456 7890</span></p>
      <p class="contact-line"><span class="contact-key">Email</span><span>abcdefgh@stayvano-example.com</span></p>
    </div>
  </section>
  <span class="stage-label stage-label-front">front</span>

  <section class="card card-back" role="img" aria-label="Card back: charcoal surface with fine vertical pinstripe texture and centred Stayvano name">
    <div class="wordmark">Stayvano<span class="wordmark-mark"></span></div>
  </section>
  <span class="stage-label stage-label-back">back</span>
</body>
</html>
```